Telecommunications/Power civil contractor needs business card design

Were a new telecommunications/power underground civil contractor that is looking for a new business card design. Our company colours are silver or grey and orange. Feel free to use the white background logo or the black background logo.

Target Market(s)

Local contractors, utility companies, private sector mining/energy companies, developers.

Industry/Entity Type

Telecommunications

Contact Information for Business Card

Each card will need the following info:
Persons name:
Title:
E-mail:
Phone number:
Shop Address:
Mailing Address:

Requirements
Must have
• Each card will need the following info:
• Persons name:
• Title:
• E-mail:
• Phone number:
• Shop Address:
• Mailing Address:

```html
<!DOCTYPE html>
<html lang="en">
<head>
<meta charset="utf-8">
<title>Business Card</title>
<link rel="stylesheet" href="https://fonts.googleapis.com/css2?family=Montserrat:wght@700;800&family=Open+Sans:wght@400;600&display=swap">
<style>
  :root {
    --page-bg: #e6e4e5;
    --card-black: #050505;
    --panel-dark: #1c1c1c;
    --panel-mid: #333333;
    --swoosh-grey: #8a8a8a;
    --swoosh-light: #b4b4b4;
    --accent-orange: #f0561d;
    --text-light: #f2f2f2;
  }
  html, body {
    margin: 0;
    width: 1200px;
    height: 1200px;
    overflow: hidden;
    background: var(--page-bg);
  }
  .canvas {
    width: 1200px;
    height: 1200px;
    display: flex;
    align-items: center;
    justify-content: center;
  }
  .business-card {
    position: relative;
    width: 1000px;
    height: 572px;
    border-radius: 44px;
    overflow: hidden;
    background: var(--card-black);
    box-shadow: 0 18px 40px rgba(0,0,0,0.25);
  }
  .card-shapes {
    position: absolute;
    inset: 0;
    width: 100%;
    height: 100%;
  }
  .brand-block {
    position: absolute;
    left: 100px;
    top: 170px;
    width: 380px;
    display: flex;
    flex-direction: column;
    align-items: center;
    gap: 20px;
  }
  .brand-mark {
    width: 96px;
    height: 96px;
    border-radius: 50%;
    background: var(--accent-orange);
    flex: none;
  }
  .brand-name {
    font-family: "Montserrat", sans-serif;
    font-weight: 800;
    color: var(--accent-orange);
    font-size: 32px;
    line-height: 1.15;
    letter-spacing: 1px;
    text-transform: uppercase;
    text-align: center;
    white-space: nowrap;
  }
  .contact-block {
    position: absolute;
    right: 60px;
    top: 52px;
    text-align: right;
    font-family: "Open Sans", sans-serif;
    color: var(--text-light);
  }
  .person-name {
    font-family: "Montserrat", sans-serif;
    font-weight: 700;
    color: var(--accent-orange);
    font-size: 38px;
    margin: 0;
    letter-spacing: 0.5px;
  }
  .person-title {
    font-size: 20px;
    margin: 2px 0 36px;
  }
  .contact-list {
    list-style: none;
    margin: 0;
    padding: 0;
  }
  .contact-item {
    display: flex;
    justify-content: flex-end;
    align-items: flex-start;
    gap: 12px;
    font-size: 20px;
    line-height: 1.4;
  }
  .contact-item.spaced { margin-top: 26px; }
  .contact-icon {
    width: 18px;
    height: 18px;
    margin-top: 6px;
    flex: none;
  }
</style>
</head>
<body>
<main class="canvas">
  <article class="business-card">
    <svg class="card-shapes" viewBox="0 0 1000 572" aria-hidden="true">
      <defs>
        <linearGradient id="panelGradient" x1="0" y1="0" x2="1" y2="1">
          <stop offset="0" stop-color="var(--panel-mid)"/>
          <stop offset="1" stop-color="var(--panel-dark)"/>
        </linearGradient>
        <linearGradient id="swooshGradient" x1="0" y1="0" x2="0" y2="1">
          <stop offset="0" stop-color="var(--swoosh-grey)"/>
          <stop offset="0.5" stop-color="var(--swoosh-light)"/>
          <stop offset="1" stop-color="var(--swoosh-grey)"/>
        </linearGradient>
      </defs>
      <rect class="contact-panel" x="0" y="0" width="1000" height="572" fill="url(#panelGradient)"/>
      <path class="swoosh-band" d="M0 0 L440 0 C610 120 620 420 560 572 L0 572 Z" fill="url(#swooshGradient)"/>
      <path class="logo-field" d="M0 0 L400 0 C560 130 570 420 515 572 L0 572 Z" fill="var(--card-black)"/>
    </svg>

    <div class="brand-block">
      <span class="brand-mark"></span>
      <span class="brand-name">Trench Line<br>Contracting Inc</span>
    </div>

    <section class="contact-block">
      <h1 class="person-name">JOHN DOE</h1>
      <p class="person-title">Director</p>
      <ul class="contact-list">
        <li class="contact-item">1-234-567890
          <svg class="contact-icon" viewBox="0 0 18 18"><circle cx="9" cy="9" r="9" fill="var(--accent-orange)"/><path d="M6 5l2 2-1 1c.6 1.3 1.7 2.4 3 3l1-1 2 2-1.5 1.5C8 13 5 10 4.5 6.5Z" fill="#fff"/></svg>
        </li>
        <li class="contact-item">john@companyname.com
          <svg class="contact-icon" viewBox="0 0 18 18"><circle cx="9" cy="9" r="9" fill="var(--accent-orange)"/><rect x="4.5" y="6" width="9" height="6" fill="#fff"/><path d="M4.5 6l4.5 3.5L13.5 6" fill="none" stroke="var(--accent-orange)" stroke-width="1"/></svg>
        </li>
        <li class="contact-item spaced"><span>123 Dummy Street<br>Dummy Centre, Dummy 12345</span>
          <svg class="contact-icon" viewBox="0 0 18 18"><circle cx="9" cy="9" r="9" fill="var(--accent-orange)"/><path d="M9 4l5 4.5h-1.5V13h-7V8.5H4Z" fill="#fff"/></svg>
        </li>
        <li class="contact-item spaced"><span>Dummy city<br>Dummy Country Land Dummy</span>
          <svg class="contact-icon" viewBox="0 0 18 18"><circle cx="9" cy="9" r="9" fill="var(--accent-orange)"/><path d="M9 3.5a3.5 3.5 0 0 1 3.5 3.5C12.5 10 9 14 9 14S5.5 10 5.5 7A3.5 3.5 0 0 1 9 3.5Z" fill="#fff"/><circle cx="9" cy="7" r="1.3" fill="var(--accent-orange)"/></svg>
        </li>
      </ul>
    </section>
  </article>
</main>
</body>
</html>
```